Web Design Project

Dear designer(s),

I need a design for a shop who's specialized into...

-Material to fix or do tailor made clothing (cloth, buttons, zippers etc)
-Curtains (static/pull-up)
-Blinds (plastic/wood)

that kind of stuff.

Good thing is that I can provide a lot of pretty photo's to work with. I have 3.5 Gigabyte of 300-1200 dpi photo's altho I converted most of them to 72dpi for your convenience (75Mb).

You can download the working material from this quellbin link:

http://files.quellbin.net/u/31920586/Velunor.zip

this is an updated file, it contains the dutch menu items to use in your design

http://files.quellbin.net/u/31920586/Velunor_Content.txt

Notice: take your time to come up with something nice. I prefer 1 or 2 designs from a designer that has been thinked of, than 5 quick ones.
Updates

Thank you for those who posted designs already but I want to clarify something.

As I mentioned it's a shop, that's a physical shop and not a webshop.

So you can safe some time and skip drawing the shopping cart icons, shop items on the homepage and other shop related things.

They don't want to start online reselling as they already spend most of their time in their shop to catch up with all orders.

Keep up the good work!

Industry/Entity Type

Clothing

Requirements
Nice to have
• Maybe the hi-res pictures can be used as background ratotor that appears left/right next to the centered website content?

Since there is a lot of material each section might have his topic linked set of thumbnails that opens a bigger image on clicking?

```html
<!DOCTYPE html>
<html lang="nl">
<head>
<meta charset="utf-8">
<title>Velunor – Stoffen, Tafellinnen, Raambekleding</title>
<link rel="stylesheet" href="https://fonts.googleapis.com/css2?family=Ubuntu:wght@300;400;500&display=swap">
<style>
  :root {
    --header-bg: #121212;
    --header-text: #f2f2f2;
    --brand-blue: #2a86b8;
    --page-bg: #f3f3f3;
    --text: #2a2a2a;
    --heading: #1e1e1e;
    --caption-bg: rgba(40, 40, 40, 0.55);
    --frame: #ffffff;
    --frame-edge: #e2e2e2;
  }
  * { box-sizing: border-box; margin: 0; padding: 0; }
  html, body { width: 1200px; height: 1176px; overflow: hidden; }
  body {
    font-family: "Ubuntu", "Segoe UI", sans-serif;
    background: var(--page-bg);
    color: var(--text);
    position: relative;
  }

  /* Header */
  .site-header {
    position: absolute; left: 0; top: 0; width: 1200px; height: 174px;
    background: var(--header-bg);
    color: var(--header-text);
  }
  .brand-name {
    position: absolute; left: 50px; top: 74px;
    display: flex; align-items: center; gap: 10px;
    font-size: 40px; font-weight: 500; color: var(--brand-blue);
    line-height: 40px; white-space: nowrap;
  }
  .brand-mark { width: 14px; height: 14px; border-radius: 50%; background: var(--brand-blue); }
  .brand-tagline {
    position: absolute; left: 282px; top: 34px;
    font-size: 15px; line-height: 19px; color: var(--header-text); white-space: nowrap;
  }
  .brand-url {
    position: absolute; left: 243px; top: 105px;
    font-size: 24px; line-height: 30px; color: var(--header-text); white-space: nowrap;
  }
  .contact {
    position: absolute; right: 46px; top: 80px; text-align: right;
    font-size: 20px; line-height: 30px; font-weight: 300;
  }

  /* Category hero */
  .categories {
    position: absolute; left: 0; top: 174px; width: 1200px; height: 412px;
    display: flex;
  }
  .category { position: relative; width: 300px; height: 412px; overflow: hidden; }
  .category + .category { border-left: 1px solid rgba(255,255,255,0.35); }
  .category-photo { position: absolute; inset: 0; }
  .photo-fabric { background: linear-gradient(135deg, #b83a6a 0%, #d9577f 45%, #8e2b4e 100%); }
  .photo-linen { background: linear-gradient(180deg, #e6d6bf 0%, #cdb48e 45%, #8a6a4a 100%); }
  .photo-decor { background: linear-gradient(160deg, #7b7b7b 0%, #b9b9b9 50%, #4a4a4a 100%); }
  .photo-blinds { background: linear-gradient(90deg, #cfd2d5 0%, #eef0f2 35%, #5a5c5f 70%, #8d9094 100%); }
  .category-caption {
    position: absolute; left: 0; bottom: 0; width: 100%; height: 56px;
    background: var(--caption-bg); color: #fff;
    font-size: 21px; font-weight: 300; text-align: center; line-height: 56px;
  }
  .category-panel {
    position: absolute; left: 0; bottom: 0; width: 100%; height: 169px;
    background: var(--caption-bg); color: #fff; padding: 12px 14px 0 16px;
  }
  .category-panel h2 { font-size: 27px; font-weight: 300; text-align: center; line-height: 34px; margin-bottom: 4px; }
  .category-panel p { font-size: 16px; line-height: 25px; font-weight: 300; }
  .panel-more { position: absolute; right: 16px; bottom: 14px; font-size: 16px; }

  /* Gallery */
  .gallery-frame {
    position: absolute; background: var(--frame);
    border: 1px solid var(--frame-edge); padding: 4px;
  }
  .gallery-frame .shot { width: 100%; height: 100%; }
  .shot-store { background: linear-gradient(120deg, #6c7b86 0%, #c9b58a 35%, #5b6fa0 65%, #e6e6ea 100%); }
  .shot-front { background: linear-gradient(180deg, #c9ced3 0%, #9aa1a8 55%, #8a5e50 100%); }
  .shot-rack { background: linear-gradient(150deg, #5d4a3a 0%, #a59b86 50%, #d2b24a 100%); }
  .shot-wall { background: linear-gradient(100deg, #c6b7a5 0%, #74685f 50%, #e4e2e0 100%); }
  .shot-counter { background: linear-gradient(170deg, #8a7a6a 0%, #b0aaa2 50%, #5a5050 100%); }
  .shot-table { background: linear-gradient(160deg, #b8a898 0%, #8a6a4a 55%, #c9a860 100%); }
  .shot-display { background: linear-gradient(180deg, #6a86a8 0%, #b9a47a 50%, #4a4a5a 100%); }
  .zoom-icon { position: absolute; right: 14px; bottom: 14px; }

  /* Intro text */
  .intro { position: absolute; left: 612px; top: 622px; width: 548px; }
  .intro h3 { font-size: 20px; font-weight: 400; color: var(--heading); line-height: 30px; }
  .intro p { font-size: 16.5px; line-height: 24.7px; margin-bottom: 8px; }
  .intro p.tight { margin-bottom: 0; }
</style>
</head>
<body>
  <header class="site-header">
    <div class="brand-tagline">Stoffen<br>Tafellinnen<br>Raambekleding</div>
    <div class="brand-name"><span class="brand-mark"></span>Velunor</div>
    <div class="brand-url">www.velunor.be</div>
    <div class="contact">Call and ask<br>Telephone: 052/73.86.20</div>
  </header>

  <nav class="categories">
    <div class="category">
      <div class="category-photo photo-fabric" role="img" aria-label="Close-up of folded pink cloth"></div>
      <div class="category-caption">Cloth - Fabric</div>
    </div>
    <div class="category">
      <div class="category-photo photo-linen" role="img" aria-label="Dining table dressed with a patterned tablecloth"></div>
      <div class="category-panel">
        <h2>Tafellinnen</h2>
        <p>Vivamus rhoncus mi pellentesque mi malesuada vehicula. In euismod nisl nec turpis faucibus nec rutrum erat interdum.</p>
        <span class="panel-more">»</span>
      </div>
    </div>
    <div class="category">
      <div class="category-photo photo-decor" role="img" aria-label="Grey curtains with a striped cushion"></div>
      <div class="category-caption">Decoratiestoffen</div>
    </div>
    <div class="category">
      <div class="category-photo photo-blinds" role="img" aria-label="Window with dark venetian blinds"></div>
      <div class="category-caption">Optreksystemen</div>
    </div>
  </nav>

  <div class="gallery-frame" style="left:47px;top:629px;width:539px;height:283px;">
    <div class="shot shot-store" role="img" aria-label="Shop interior with walls of buttons and haberdashery"></div>
    <svg class="zoom-icon" width="14" height="14" viewBox="0 0 14 14" aria-hidden="true">
      <circle cx="7" cy="7" r="6" fill="rgba(255,255,255,0.6)"/>
      <path d="M7 4v6M4 7h6" stroke="#555" stroke-width="1.4"/>
    </svg>
  </div>
  <div class="gallery-frame" style="left:47px;top:935px;width:166px;height:106px;">
    <div class="shot shot-front" role="img" aria-label="Shop front seen from the street"></div>
  </div>
  <div class="gallery-frame" style="left:235px;top:935px;width:166px;height:106px;">
    <div class="shot shot-rack" role="img" aria-label="Rack of haberdashery items"></div>
  </div>
  <div class="gallery-frame" style="left:426px;top:935px;width:160px;height:106px;">
    <div class="shot shot-wall" role="img" aria-label="Wall of button drawers"></div>
  </div>
  <div class="gallery-frame" style="left:44px;top:1056px;width:170px;height:106px;">
    <div class="shot shot-counter" role="img" aria-label="Shop counter with staff"></div>
  </div>
  <div class="gallery-frame" style="left:237px;top:1056px;width:160px;height:106px;">
    <div class="shot shot-table" role="img" aria-label="Fabric being measured on a cutting table"></div>
  </div>
  <div class="gallery-frame" style="left:473px;top:1056px;width:66px;height:106px;">
    <div class="shot shot-display" role="img" aria-label="Rotating thread display stand"></div>
  </div>

  <section class="intro">
    <h3>Nullam eu ornare</h3>
    <p class="tight">Sed a tortor eget sapien porttitor consectetur. Cum sociis natoque penatibus et magnis dis parturient montes, nascetur ridiculus mus. Mauris vitae blandit mauris. Aenean rhoncus purus vel odio posuere at elementum mauris tincidunt.</p>
    <h3>Etiam in arcu metus</h3>
    <p>Porttitor fringilla mi. Mauris eu ipsum lorem, sit amet vehicula lorem. Aenean dictum, lacus ut luctus laoreet, est metus vehicula nulla, id fermentum lacus lectus in dui.</p>
    <p>Vestibulum ante ipsum primis in faucibus orci luctus et ultrices posuere cubilia Curae. Suspendisse ullamcorper porttitor nunc sed imperdiet. Nunc vulputate sem sed turpis fermentum accumsan.</p>
    <p class="tight">Nulla facilisis orci non sapien tristique aliquet. In mattis euismod lorem, eu tristique dolor aliquet nec. Nullam gravida.</p>
    <p>Mauris tempor lacinia condimentum. Class aptent taciti sociosqu ad litora</p>
  </section>
</body>
</html>
```